Audio-Visual & Video Communications Business Requires a Cutting-edge Business Card Design

LinkHarbor is a new Audio-Visual & Video Communications company in Cape Town, South Africa that is looking for a cutting-edge business card design. We sell these products to the Corporate, Education & Hospitality markets and will also host an Online Shop for companies and individuals to purchase our products online.

We are already using the following two colours in our logo and draft website. Please incorporate these colours into the design. Please note that our website is still in the design stage if you need to visit it. Green #a0ce4e & Dark Grey #333333.
Updates

Hi,

Please note that I have uploaded our logo in an .eps format.

Target Market(s)

Corporate Companies, Education Institutions & Hospitality Markets

Industry/Entity Type

Business

Requirements
Nice to have
• It would be great if you could incorporate the services that we offer.

1. Consultation & Design
2. Project Management
3. Supply & Installation
4. Onsite Support Personal
5. Online Shop

```html
<!DOCTYPE html>
<html lang="en">
<head>
<meta charset="utf-8">
<title>LinkHarbor – Business Card</title>
<link href="https://fonts.googleapis.com/css2?family=Open+Sans:wght@400;700&display=swap" rel="stylesheet">
<style>
  :root {
    --backdrop: #3b3b3b;
    --card-front: #ffffff;
    --card-front-edge: #e4e4e4;
    --card-back: #5b5b5b;
    --brand-green: #a0ce4e;
    --brand-grey: #333333;
    --text-light: #ffffff;
  }
  html, body {
    margin: 0;
    padding: 0;
    width: 1200px;
    height: 960px;
    overflow: hidden;
    background: var(--backdrop);
    font-family: "Open Sans", Arial, sans-serif;
  }
  .canvas {
    position: relative;
    width: 1200px;
    height: 960px;
  }
  .bubbles {
    position: absolute;
    inset: 0;
  }
  .brand {
    position: absolute;
    left: 262px;
    top: 300px;
    display: flex;
    align-items: center;
    gap: 12px;
    transform: rotate(7deg);
    transform-origin: left center;
  }
  .brand-dot {
    width: 26px;
    height: 26px;
    border-radius: 50%;
    background: var(--brand-green);
  }
  .brand-name {
    font-size: 46px;
    font-weight: 700;
    color: var(--brand-grey);
    letter-spacing: -0.5px;
  }
  .contact-list {
    position: absolute;
    left: 586px;
    top: 478px;
    margin: 0;
    padding: 0;
    list-style: none;
    transform: rotate(-9deg);
    transform-origin: left top;
  }
  .contact-item {
    display: flex;
    align-items: center;
    gap: 14px;
    height: 44px;
    color: var(--text-light);
    font-size: 19px;
    letter-spacing: 0.3px;
  }
  .contact-icon {
    width: 32px;
    height: 32px;
    flex: none;
  }
</style>
</head>
<body>
<main class="canvas">
  <svg class="bubbles" width="1200" height="960" viewBox="0 0 1200 960" aria-hidden="true">
    <defs>
      <radialGradient id="front-shade" cx="0.5" cy="0.5" r="0.5">
        <stop offset="0.8" stop-color="var(--card-front)"/>
        <stop offset="1" stop-color="var(--card-front-edge)"/>
      </radialGradient>
    </defs>
    <g class="card-back">
      <circle cx="741" cy="544" r="211" fill="var(--card-back)"/>
      <polygon points="790,700 902,825 868,690" fill="var(--card-back)"/>
    </g>
    <g class="card-front">
      <polygon points="300,480 260,630 395,545" fill="var(--card-front-edge)"/>
      <circle cx="411" cy="333" r="211" fill="url(#front-shade)"/>
    </g>
  </svg>

  <div class="brand">
    <span class="brand-dot"></span>
    <span class="brand-name">LinkHarbor</span>
  </div>

  <ul class="contact-list">
    <li class="contact-item">
      <svg class="contact-icon" viewBox="0 0 32 32" fill="none" stroke="#fff" stroke-width="2">
        <rect x="3" y="6" width="8" height="22" rx="3"/>
        <rect x="11" y="10" width="18" height="18" rx="2"/>
        <path d="M15 15h2M20 15h2M25 15h0M15 19h2M20 19h2M15 23h2M20 23h2"/>
      </svg>
      <span>+27 21 555-0147</span>
    </li>
    <li class="contact-item">
      <svg class="contact-icon" viewBox="0 0 32 32" fill="none" stroke="#fff" stroke-width="2">
        <rect x="10" y="11" width="11" height="19" rx="2"/>
        <path d="M13 16h5M13 21h5M13 25h5"/>
        <path d="M12 7a6 6 0 0 1 7 0M9 4a10 10 0 0 1 13 0"/>
      </svg>
      <span>+27 82 555-0193</span>
    </li>
    <li class="contact-item">
      <svg class="contact-icon" viewBox="0 0 32 32" fill="none" stroke="#fff" stroke-width="2">
        <rect x="3" y="8" width="26" height="18" rx="1"/>
        <path d="M3 9l13 10 13-10M3 26l10-9M29 26l-10-9"/>
      </svg>
      <span>me@linkharbor.co.za</span>
    </li>
    <li class="contact-item">
      <svg class="contact-icon" viewBox="0 0 32 32" fill="none" stroke="#fff" stroke-width="2">
        <circle cx="16" cy="16" r="13"/>
        <ellipse cx="16" cy="16" rx="6" ry="13"/>
        <path d="M3 16h26M5 9h22M5 23h22"/>
      </svg>
      <span>www.linkharbor.co.za</span>
    </li>
  </ul>
</main>
</body>
</html>
```